Structural Engineering Business Card

Veltrow Drafts does residential house plans for clients in Central Florida. Would like simple but elegant business card that is appropriate for a house plan engineering company. Prefer black business card with black/white them but open to other shades of blue. I uploaded a sample card that I came across that looked good but please come up with your own creative designs.

Contact Information for Business Card

Name, Title, Phone, Email, Address, website

```html
<!DOCTYPE html>
<html lang="en">
<head>
<meta charset="utf-8">
<title>Veltrow Drafts – Business Card</title>
<link href="https://fonts.googleapis.com/css2?family=Montserrat:wght@500;700&display=swap" rel="stylesheet">
<style>
  :root {
    --page-bg: #d9d9d9;
    --card-dark: #2b2b2b;
    --card-mid: #313131;
    --ink: #ffffff;
  }
  html, body {
    margin: 0;
    width: 1200px;
    height: 1200px;
    overflow: hidden;
    background: var(--page-bg);
    font-family: "Montserrat", sans-serif;
    color: var(--ink);
  }
  .card {
    position: absolute;
    left: 220px;
    width: 760px;
    height: 436px;
    border-radius: 19px;
    overflow: hidden;
    background: var(--card-dark);
  }
  .card--front { top: 124px; }
  .card--back { top: 640px; }
  .blueprint-backdrop {
    position: absolute;
    inset: 0;
    background: radial-gradient(ellipse at 45% 45%, var(--card-mid) 0%, var(--card-dark) 75%);
  }
  .brand-name {
    position: absolute;
    margin: 0;
    font-weight: 700;
    line-height: 1;
    white-space: nowrap;
    letter-spacing: 0.5px;
  }
  .card--front .brand-name {
    left: 44px;
    top: 198px;
    font-size: 37px;
  }
  .card--back .brand-name {
    left: 0;
    right: 0;
    top: 188px;
    text-align: center;
    font-size: 58px;
  }
  .divider {
    position: absolute;
    left: 378px;
    top: 121px;
    width: 2px;
    height: 196px;
    background: var(--ink);
  }
  .person {
    position: absolute;
    left: 419px;
    top: 116px;
  }
  .person-name {
    margin: 0;
    font-size: 22px;
    font-weight: 700;
    letter-spacing: 0.8px;
  }
  .person-title {
    margin: 4px 0 0;
    font-size: 18px;
    font-weight: 500;
    letter-spacing: 0.3px;
  }
  .contact-list {
    position: absolute;
    left: 419px;
    top: 185px;
    margin: 0;
    padding: 0;
    list-style: none;
    font-size: 18px;
    font-weight: 500;
    letter-spacing: 0.3px;
  }
  .contact-item {
    display: flex;
    align-items: flex-start;
    line-height: 26px;
  }
  .contact-item + .contact-item { margin-top: 0; }
  .contact-item--address { margin-bottom: 10px; }
  .contact-icon {
    width: 16px;
    height: 16px;
    margin: 5px 8px 0 0;
    flex: none;
  }
</style>
</head>
<body>
  <section class="card card--front">
    <div class="blueprint-backdrop" role="img" aria-label="Faint architectural house elevation and floor plan drawings in dark grey"></div>
    <p class="brand-name">Veltrow Drafts</p>
    <div class="divider"></div>
    <div class="person">
      <h1 class="person-name">DORIAN HALVEK</h1>
      <p class="person-title">General Manager</p>
    </div>
    <ul class="contact-list">
      <li class="contact-item contact-item--address">
        <svg class="contact-icon" viewBox="0 0 16 16" fill="none" stroke="#fff" stroke-width="1.4"><path d="M8 15s5-5.2 5-8.8A5 5 0 0 0 3 6.2C3 9.8 8 15 8 15z"/><circle cx="8" cy="6.2" r="1.8"/></svg>
        <span>Marlowe Ave. Suite No. 22<br>Ashgrove City, FL 340219</span>
      </li>
      <li class="contact-item">
        <svg class="contact-icon" viewBox="0 0 16 16" fill="#fff"><path d="M3.2 1.5l2.3 2.8-1.3 1.6c.9 2 2.4 3.5 4.4 4.4l1.6-1.3 2.8 2.3-1.4 2.2C6.6 15 1 9.4 1.5 3l1.7-1.5z"/></svg>
        <span>000-555-218436</span>
      </li>
      <li class="contact-item">
        <svg class="contact-icon" viewBox="0 0 16 16" fill="#fff"><path d="M1 3.5h14v9H1z M1.6 4.1L8 9l6.4-4.9" stroke="#2b2b2b" stroke-width="1"/></svg>
        <span>info@veltrowdrafts.com</span>
      </li>
      <li class="contact-item">
        <svg class="contact-icon" viewBox="0 0 16 16" fill="none" stroke="#fff" stroke-width="1.1"><circle cx="8" cy="8" r="6.6"/><ellipse cx="8" cy="8" rx="2.8" ry="6.6"/><path d="M1.4 8h13.2M2.6 4.5h10.8M2.6 11.5h10.8"/></svg>
        <span>www.veltrowdrafts.com</span>
      </li>
    </ul>
  </section>

  <section class="card card--back">
    <div class="blueprint-backdrop" role="img" aria-label="Faint architectural house elevation and floor plan drawings in dark grey"></div>
    <p class="brand-name">Veltrow Drafts</p>
  </section>
</body>
</html>
```